Website for Apartment Rental in Prague

I would like to create designs of my website focused on luxury apartment rentals in Prague, Czech Republic. I created initial mock-ups, They are all attached. I need to design homepage and subpage. The mock-ups were created by combining elements from different websites that I liked but I need you to create a design that is unique and original. The attached files a only a guidance for the structure of the website but not for the design. Try to be creative.

Industry/Entity Type

Apartment

```html
<!DOCTYPE html>
<html lang="en">
<head>
<meta charset="utf-8">
<title>Belle Nuit Apartments Prague</title>
<link rel="stylesheet" href="https://fonts.googleapis.com/css2?family=Cormorant+Garamond:wght@500;600&family=Jost:wght@300;400;500;600&display=swap">
<style>
:root{
  --gold:#a98a62;
  --gold-soft:#c9b08c;
  --espresso:#2f2822;
  --espresso-2:#3d342c;
  --ink:#1f1b18;
  --text:#5a534c;
  --muted:#9a928a;
  --line:#e6e0d8;
  --paper:#fff;
  --linen:#f6f2ec;
  --band:#ece6dd;
  --stone:#cfc6ba;
}
*{margin:0;padding:0;box-sizing:border-box}
html,body{width:1200px;height:2605px;overflow:hidden}
body{position:relative;background:var(--paper);font-family:"Jost",Arial,sans-serif;color:var(--text)}
.abs{position:absolute}
.serif{font-family:"Cormorant Garamond",Georgia,serif}

/* top bar */
.topbar{left:0;top:0;width:1200px;height:61px;font-size:11.5px;letter-spacing:1px;color:var(--ink);text-transform:uppercase}
.topbar .item{position:absolute;top:21px;white-space:nowrap}
.topbar svg{vertical-align:-1px;margin-right:6px}
.brand{position:absolute;left:450px;top:6px;width:300px;text-align:center}
.brand-name{font-family:"Cormorant Garamond",serif;font-weight:600;font-size:25px;line-height:26px;color:var(--gold);letter-spacing:1px}
.brand-sub{font-size:10px;letter-spacing:3px;color:var(--ink);margin-top:2px}

.mainnav{left:0;top:61px;width:1200px;height:47px;border-top:1px solid var(--line);border-bottom:1px solid var(--line)}
.mainnav ul{list-style:none;display:flex;justify-content:space-between;align-items:center;height:100%;padding:0 122px;font-size:13px;font-weight:500;letter-spacing:1.2px;color:var(--ink)}

/* hero */
.hero{left:0;top:108px;width:1200px;height:521px;background:linear-gradient(105deg,#3a3632 0%,#6f6a64 22%,#cfc9c0 46%,#b9b2a8 60%,#5d5852 80%,#b0875a 100%)}
.hero-shade{left:0;top:108px;width:1200px;height:521px;background:linear-gradient(180deg,rgba(30,25,20,0) 40%,rgba(30,25,20,.35) 100%)}
.hero-title{left:0;top:330px;width:1200px;text-align:center;font-family:"Cormorant Garamond",serif;font-weight:500;font-size:44px;letter-spacing:6px;color:#fff;text-transform:uppercase}
.booking{left:113px;top:425px;width:974px;height:150px;background:rgba(255,255,255,.96);border-top:3px solid var(--gold)}
.booking h2{position:absolute;top:14px;width:100%;text-align:center;font-family:"Cormorant Garamond",serif;font-weight:600;font-size:28px;letter-spacing:2px;color:var(--gold)}
.field{position:absolute;top:68px}
.field label{display:block;font-size:11px;letter-spacing:.3px;color:var(--ink);height:14px;margin-bottom:8px;white-space:nowrap}
.field .box{height:40px;border:none;border-bottom:1px solid var(--stone);background:var(--linen);font-size:12px;color:var(--ink);padding:12px 8px;position:relative}
.field .box.sel:after{content:"";position:absolute;right:6px;top:16px;width:6px;height:6px;border-right:1px solid var(--gold);border-bottom:1px solid var(--gold);transform:rotate(45deg)}
.check-btn{position:absolute;left:679px;top:90px;width:141px;height:40px;background:var(--espresso);color:#fff;font-size:11.5px;letter-spacing:.6px;font-weight:500;text-align:center;line-height:40px}
.or{position:absolute;left:826px;top:103px;font-size:11px;color:var(--muted)}
.unit{position:absolute;left:846px;top:90px;width:113px;height:40px;background:var(--linen);border-bottom:1px solid var(--stone);font-size:10.5px;line-height:40px;padding-left:7px;color:var(--ink);white-space:nowrap}

/* intro */
.linen{left:0;top:629px;width:1200px;height:1064px;background:var(--linen)}
.intro-title{left:0;top:668px;width:1200px;text-align:center;font-family:"Cormorant Garamond",serif;font-weight:500;font-size:44px;color:var(--ink)}
.intro-rule{left:560px;top:740px;width:80px;height:1px;background:var(--gold)}
.intro-lead{left:140px;top:768px;width:920px;text-align:center;font-style:italic;font-weight:300;font-size:13px;line-height:23px;color:var(--gold)}
.badge{left:562px;top:856px;width:76px;height:76px;border-radius:50%;background:var(--gold);box-shadow:0 0 0 6px var(--linen),0 0 0 7px var(--gold-soft)}
.badge svg{position:absolute;left:22px;top:18px}
.badge-cap{left:0;top:941px;width:1200px;text-align:center;font-size:16px;line-height:23px;color:var(--text)}
.badge-cap b{font-weight:500;color:var(--ink)}
.intro-body{left:135px;top:1002px;width:930px;text-align:center;font-size:14.5px;font-weight:300;line-height:23px;color:var(--text)}
.divider{left:122px;top:1180px;width:956px;height:1px;background:var(--stone)}

/* cards */
.card{background:#fff;border:1px solid var(--line)}
.card .photo{position:absolute;left:0;top:0;width:100%}
.heart{position:absolute;top:12px;right:12px;width:30px;height:30px;border-radius:50%;background:#fff;display:flex;align-items:center;justify-content:center}
.card h3{position:absolute;font-family:"Cormorant Garamond",serif;font-weight:600;font-size:17px;color:var(--ink);white-space:nowrap}
.card .price{position:absolute;font-size:14px;font-weight:600;color:var(--gold);white-space:nowrap}
.card .price small{font-weight:400;font-size:12px}
.card .addr{position:absolute;font-size:10px;color:var(--muted);white-space:nowrap}
.card .addr svg{vertical-align:-1px;margin-right:3px}
.stats{position:absolute;display:flex;gap:18px}
.stat b{display:block;font-weight:400;font-size:19px;line-height:22px;color:var(--ink)}
.stat b sup{font-size:11px}
.stat i{font-style:normal;font-size:8px;letter-spacing:.8px;color:var(--muted)}
.details{position:absolute;width:115px;height:31px;border:1px solid var(--gold);color:var(--gold);font-size:10px;font-weight:600;letter-spacing:1px;text-align:center;line-height:29px}

.featured-title{left:0;top:1712px;width:1200px;text-align:center;font-family:"Cormorant Garamond",serif;font-weight:600;font-size:30px;color:var(--ink)}

/* partners */
.partners{left:0;top:2181px;width:1200px;height:116px;background:var(--band)}
.partner{position:absolute;top:45px;height:26px;background:var(--stone)}

/* footer */
.footer{left:0;top:2297px;width:1200px;height:247px;background:var(--espresso);color:#efe8de}
.footer h4{position:absolute;top:48px;font-family:"Cormorant Garamond",serif;font-weight:500;font-size:27px;letter-spacing:1px;color:var(--gold-soft);white-space:nowrap}
.footer ul{position:absolute;top:110px;list-style:none;font-size:14px;letter-spacing:1px;line-height:33px;text-transform:uppercase}
.email{position:absolute;left:764px;top:110px;width:195px;height:42px;background:transparent;border:1px solid var(--gold-soft);color:#efe8de;font-size:12px;letter-spacing:1px;line-height:40px;padding-left:14px}
.signup{position:absolute;left:959px;top:110px;width:111px;height:42px;background:var(--gold);color:#fff;font-size:15px;font-weight:500;letter-spacing:1.5px;text-align:center;line-height:42px}
.social{position:absolute;top:176px;width:31px;height:31px;border:1px solid var(--gold-soft);border-radius:50%}
.bottombar{left:0;top:2544px;width:1200px;height:61px;background:var(--espresso-2);color:#d9cfc2}
.copy{position:absolute;left:125px;top:22px;font-size:13px;letter-spacing:.3px}
.chat{position:absolute;left:750px;top:21px;width:320px;height:40px;background:var(--gold);color:#fff;font-size:13px;letter-spacing:.5px;line-height:40px;padding-left:14px}
.chat .ctl{position:absolute;top:12px;width:16px;height:16px;background:#fff;color:var(--gold);font-size:12px;line-height:16px;text-align:center;font-weight:600}
</style>
</head>
<body>

<header class="abs topbar">
  <span class="item" style="left:122px">Our Hospitality</span>
  <span class="item" style="left:255px">EN <svg width="8" height="6" viewBox="0 0 8 6"><path d="M1 1l3 3 3-3" stroke="#1f1b18" fill="none"/></svg></span>
  <span class="item" style="left:320px">Discover Prague</span>
  <div class="brand"><div class="brand-name">Belle Nuit</div><div class="brand-sub">APARTMENTS PRAGUE</div></div>
  <span class="item" style="left:745px;text-transform:none;letter-spacing:.3px"><svg width="13" height="10" viewBox="0 0 13 10"><rect x=".5" y=".5" width="12" height="9" fill="none" stroke="#a98a62"/><path d="M.5.5l6 4.5 6-4.5" stroke="#a98a62" fill="none"/></svg>reservation@bellenuitstays.com</span>
  <span class="item" style="left:968px;letter-spacing:.3px"><svg width="11" height="11" viewBox="0 0 11 11"><path d="M2 0l2 2.5-1 1.5c1 1.5 2 2.5 3.5 3.5l1.5-1L11 9l-1.5 2C5 10.5.5 6 0 1.5z" fill="#a98a62"/></svg>+420 700 318 264</span>
</header>

<nav class="abs mainnav">
  <ul><li>APARTMENTS</li><li>LOCATIONS</li><li>SERVICES</li><li>GALLERY</li><li>NEWS</li><li>EXCLUSIVE OFFER &amp; TOURS</li><li>FOR FAMILIES</li><li>CONTACT US</li></ul>
</nav>

<div class="abs hero" role="img" aria-label="Photo of a bright modern apartment living room with sofa, dining table and a terrace at sunset"></div>
<div class="abs hero-shade"></div>
<h1 class="abs hero-title">Being Home in Prague</h1>

<form class="abs booking">
  <h2>OFFICIAL SITE - BEST PRICE GUARANTEED</h2>
  <div class="field" style="left:15px;width:134px"><label>Check in date</label><div class="box">11/17/2017</div></div>
  <div class="field" style="left:156px;width:136px"><label>Check out date</label><div class="box">11/18/2017</div></div>
  <div class="field" style="left:299px;width:56px"><label>Adults</label><div class="box sel">2</div></div>
  <div class="field" style="left:364px;width:58px"><label>Children</label><div class="box sel">0</div></div>
  <div class="field" style="left:431px;width:57px"><label>Infants</label><div class="box sel">0</div></div>
  <div class="field" style="left:495px;width:177px"><label>Promotional Code</label><div class="box"></div></div>
  <div class="check-btn">Check Availability</div>
  <div class="or">OR</div>
  <div class="unit">Select Rental Unit ⌄</div>
</form>

<section>
  <div class="abs linen"></div>
  <h2 class="abs intro-title">A Different Vision of Traveling</h2>
  <div class="abs intro-rule"></div>
  <p class="abs intro-lead">Lorem ipsum dolor sit amet, consectetuer adipiscing elit, sed diam nonummy nibh euismod tincidunt ut laoreet dolore magna aliquam erat volutpat. Ut wisi enim ad minim veniam, quis nostrud exerci tation ullamcorper suscipit lobortis nisl ut aliquip ex ea commodo consequat. Duis autem vel eum iriure dolor in hendrerit in vulputate velit esse molestie consequat</p>
  <div class="abs badge"><svg width="32" height="40" viewBox="0 0 32 40" fill="none" stroke="#fff" stroke-width="1.6"><rect x="6" y="2" width="20" height="18" rx="2"/><path d="M11 5v12M16 5v12M21 5v12M3 20h26v5H3zM6 25v13M26 25v13M8 32h16"/></svg></div>
  <p class="abs badge-cap">Interiors Designed<br><b>By Belle Nuit</b></p>
  <p class="abs intro-body">Duis autem vel eum iriure dolor in hendrerit in vulputate velit esse molestie consequat, vel illum dolore eu feugiat nulla facilisis at vero eros et accumsan et iusto odio dignissim qui blandit praesent luptatum zzril delenit augue duis dolore te feugait nulla facilisi. Nam liber tempor cum soluta nobis eleifend option congue nihil imperdiet doming id quod mazim placerat facer possim assum. Typi non habent claritatem insitam; est usus legentis in iis qui facit eorum claritatem. Investigationes demonstraverunt lectores legere me lius quod ii legunt saepius.</p>
  <div class="abs divider"></div>

  <article class="abs card" style="left:111px;top:1236px;width:474px;height:414px">
    <div class="photo" style="height:292px;background:linear-gradient(180deg,#5a5d9a 0%,#a07aa8 35%,#9aa0a0 62%,#4f5a45 100%)" role="img" aria-label="Photo of a white villa with a garage at dusk"></div>
    <div class="heart"><svg width="14" height="12" viewBox="0 0 14 12"><path d="M7 11S1 7 1 3.5A3 3 0 0 1 7 2.5 3 3 0 0 1 13 3.5C13 7 7 11 7 11z" stroke="#a98a62" fill="none"/></svg></div>
    <h3 style="left:16px;top:302px">Real House Luxury Villa</h3>
    <div class="price" style="right:16px;top:305px">$2,285,500</div>
    <div class="addr" style="left:16px;top:329px"><svg width="7" height="9" viewBox="0 0 7 9"><path d="M3.5 9S0 5 0 3.5a3.5 3.5 0 0 1 7 0C7 5 3.5 9 3.5 9z" fill="#9a928a"/></svg>24 Vinohradska St, 12 - Prague 2, CZ</div>
    <div class="stats" style="left:16px;top:362px"><div class="stat"><b>5<sup>+</sup></b><i>BEDS</i></div><div class="stat"><b>3</b><i>BATHS</i></div><div class="stat"><b>1,250</b><i>SQ.FT</i></div></div>
    <div class="details" style="right:16px;top:365px">DETAILS ›</div>
  </article>

  <article class="abs card" style="left:611px;top:1236px;width:476px;height:414px">
    <div class="photo" style="height:292px;background:linear-gradient(180deg,#3b4254 0%,#5a5e66 45%,#8a5b3a 70%,#2a8fd8 100%)" role="img" aria-label="Photo of a modern house with a lit pool at night"></div>
    <div class="heart"><svg width="14" height="12" viewBox="0 0 14 12"><path d="M7 11S1 7 1 3.5A3 3 0 0 1 7 2.5 3 3 0 0 1 13 3.5C13 7 7 11 7 11z" stroke="#a98a62" fill="none"/></svg></div>
    <h3 style="left:16px;top:302px">House Take Away</h3>
    <div class="price" style="right:16px;top:305px">$2,285,500</div>
    <div class="addr" style="left:16px;top:329px"><svg width="7" height="9" viewBox="0 0 7 9"><path d="M3.5 9S0 5 0 3.5a3.5 3.5 0 0 1 7 0C7 5 3.5 9 3.5 9z" fill="#9a928a"/></svg>24 Vinohradska St, 12 - Prague 2, CZ</div>
    <div class="stats" style="left:16px;top:362px"><div class="stat"><b>5<sup>+</sup></b><i>BEDS</i></div><div class="stat"><b>3</b><i>BATHS</i></div><div class="stat"><b>1,250</b><i>SQ.FT</i></div></div>
    <div class="details" style="right:16px;top:365px">DETAILS ›</div>
  </article>
</section>

<section>
  <h2 class="abs featured-title">Featured Listing</h2>

  <article class="abs card" style="left:57px;top:1764px;width:309px;height:344px">
    <div class="photo" style="height:190px;background:linear-gradient(180deg,#5a5d9a 0%,#a07aa8 35%,#9aa0a0 62%,#4f5a45 100%)" role="img" aria-label="Photo of a white villa with a garage at dusk"></div>
    <div class="heart"><svg width="14" height="12" viewBox="0 0 14 12"><path d="M7 11S1 7 1 3.5A3 3 0 0 1 7 2.5 3 3 0 0 1 13 3.5C13 7 7 11 7 11z" stroke="#a98a62" fill="none"/></svg></div>
    <h3 style="left:16px;top:198px">Real House Luxury Villa</h3>
    <div class="addr" style="left:16px;top:224px"><svg width="7" height="9" viewBox="0 0 7 9"><path d="M3.5 9S0 5 0 3.5a3.5 3.5 0 0 1 7 0C7 5 3.5 9 3.5 9z" fill="#9a928a"/></svg>24 Vinohradska St, 12 - Prague 2, CZ</div>
    <div class="price" style="left:16px;top:245px">$2,285,500</div>
    <div class="stats" style="left:16px;top:290px"><div class="stat"><b>5<sup>+</sup></b><i>BEDS</i></div><div class="stat"><b>3</b><i>BATHS</i></div><div class="stat"><b>1,250</b><i>SQ.FT</i></div></div>
    <div class="details" style="right:16px;top:292px">DETAILS ›</div>
  </article>

  <article class="abs card" style="left:392px;top:1764px;width:310px;height:344px">
    <div class="photo" style="height:190px;background:linear-gradient(180deg,#3b4254 0%,#5a5e66 45%,#8a5b3a 70%,#2a8fd8 100%)" role="img" aria-label="Photo of a modern house with a lit pool at night"></div>
    <div class="heart"><svg width="14" height="12" viewBox="0 0 14 12"><path d="M7 11S1 7 1 3.5A3 3 0 0 1 7 2.5 3 3 0 0 1 13 3.5C13 7 7 11 7 11z" stroke="#a98a62" fill="none"/></svg></div>
    <h3 style="left:16px;top:198px">House Take Away</h3>
    <div class="addr" style="left:16px;top:224px"><svg width="7" height="9" viewBox="0 0 7 9"><path d="M3.5 9S0 5 0 3.5a3.5 3.5 0 0 1 7 0C7 5 3.5 9 3.5 9z" fill="#9a928a"/></svg>24 Vinohradska St, 12 - Prague 2, CZ</div>
    <div class="price" style="left:16px;top:245px">$85,500<small>/ Month</small></div>
    <div class="stats" style="left:16px;top:290px"><div class="stat"><b>5<sup>+</sup></b><i>BEDS</i></div><div class="stat"><b>3</b><i>BATHS</i></div><div class="stat"><b>1,250</b><i>SQ.FT</i></div></div>
    <div class="details" style="right:16px;top:292px">DETAILS ›</div>
  </article>

  <article class="abs card" style="left:726px;top:1764px;width:309px;height:344px">
    <div class="photo" style="height:190px;background:linear-gradient(180deg,#9cc4e8 0%,#dfe6ea 40%,#7aa05a 75%,#3aa7d6 100%)" role="img" aria-label="Photo of a white modern villa with a pool and lawn"></div>
    <div class="heart"><svg width="14" height="12" viewBox="0 0 14 12"><path d="M7 11S1 7 1 3.5A3 3 0 0 1 7 2.5 3 3 0 0 1 13 3.5C13 7 7 11 7 11z" stroke="#a98a62" fill="none"/></svg></div>
    <h3 style="left:16px;top:198px">Willow Heights Place</h3>
    <div class="addr" style="left:16px;top:224px"><svg width="7" height="9" viewBox="0 0 7 9"><path d="M3.5 9S0 5 0 3.5a3.5 3.5 0 0 1 7 0C7 5 3.5 9 3.5 9z" fill="#9a928a"/></svg>24 Vinohradska St, 12 - Prague 2, CZ</div>
    <div class="price" style="left:16px;top:245px">REQUEST PRICE</div>
    <div class="stats" style="left:16px;top:290px"><div class="stat"><b>5<sup>+</sup></b><i>BEDS</i></div><div class="stat"><b>3</b><i>BATHS</i></div><div class="stat"><b>1,250</b><i>SQ.FT</i></div></div>
    <div class="details" style="right:16px;top:292px">DETAILS ›</div>
  </article>
</section>

<div class="abs partners" aria-label="Partners">
  <div class="partner" style="left:145px;width:122px"></div>
  <div class="partner" style="left:340px;width:122px"></div>
  <div class="partner" style="left:538px;width:122px"></div>
  <div class="partner" style="left:730px;width:126px"></div>
  <div class="partner" style="left:937px;width:102px"></div>
</div>

<footer class="abs footer">
  <h4 style="left:125px">OUR INFO</h4>
  <h4 style="left:304px">BOOKING</h4>
  <h4 style="left:478px">ADDITIONAL LINKS</h4>
  <h4 style="left:764px">STAY CONNECTED</h4>
  <ul style="left:127px"><li>Homepage</li><li>About Us</li><li>Hiring</li></ul>
  <ul style="left:306px"><li>Booking Page</li><li>Blog</li></ul>
  <ul style="left:480px"><li>Gift Card</li><li>Help</li><li>We're Green</li></ul>
  <div class="email">EMAIL</div>
  <div class="signup">SIGN UP</div>
  <div class="social" style="left:764px"></div>
  <div class="social" style="left:804px"></div>
  <div class="social" style="left:845px"></div>
  <div class="social" style="left:885px"></div>
</footer>

<div class="abs bottombar">
  <p class="copy">Copyright Interiors Designed By Belle Nuit @2017</p>
  <div class="chat">Live Chat<span class="ctl" style="left:276px">⌄</span><span class="ctl" style="left:298px">+</span></div>
</div>

</body>
</html>
```